Web Design Project

Hi,
I am building a web based business within the wedding industry and I am looking for someone to design the front page of the website for me as well as the following pages/categroires which all need to be supportive of the front page
The screens will be:
Home
One Stop Reistry
Wedding Deals
Travel/Getaway
Wedding marketplace
Blog
Contact US
A more detailed view of the above is as follows:
1. Home page - be bright and capture an audience
2. Aggregate gift registries ie from key online retailers so people visiting my site can set up a bridal registry from numerous stores all in the one place ie: http://www.harlowbrent.com.au/, http://www.quillo.com.au/, http://www.kvsonic.com.au/ http://www.felixramsay.com.au/ Something similar to http://www.vowpresentsnow.com.au
3. Aggregate the deal sites to pull all the deals relating to weddings ie: hair and make up, travel, car hire, venue hire, waxing, laser, facials, beauty treatments. Similar to http://www.pennysaverhub.com.au/daily-deals or http://www.ringbargains.com.au/
3. We will have a tab for travel and accommodation which we want to pull the info from Voyaro which I believe you can become a member and do so quite easily http://www.voyaro.com.au/daily/service/affiliate-program.aspx
4. We want to build like our own tradlo/marketplace within the site where people can list things like their wedding dress, gifts they don’t want or need etc similar to http://www.gownagain.com/
5. A blog tab where we can have blogs/gossip section and build a forum for people to discuss wedding related issues similar to http://www.altartalk.com/wedding-forums or http://veilnest.com.au/Forums or gossip like http://www.starlettechatter.com/categories/celebrity-weddings/ The look of this section could be designed to look a bit like a gossip magazine
People need to be able to log in and out of the site and it needs to be able to be connected with pallbook and workvine as well as allowing people to subscribe to a mailing list and unsubscribe if required.
I have done a quick mock-up on powerpoint with what needs to be included but needs a lot of changing. Can be any pictures and what I have attached is not an ide ajust essentials to be on the page.
A good site to give you an idea is http://thebouquet.sevenweb.com.au/

```html
<!DOCTYPE html>
<html lang="en">
<head>
<meta charset="utf-8">
<title>Wedding Gleam – Login</title>
<link rel="stylesheet" href="https://fonts.googleapis.com/css2?family=Ubuntu:ital,wght@0,400;0,500;0,700;1,400&family=Yesteryear&family=Courgette&display=swap">
<style>
  :root {
    --page-bg: #f3f2f0;
    --brown: #7e3f22;
    --brown-light: #a65c33;
    --brown-dark: #6c341b;
    --tan: #c8a06e;
    --tan-soft: #d9bf9c;
    --text-dark: #3a2a20;
    --text-mid: #5a4a40;
    --field-border: #e2ddd6;
    --white: #ffffff;
  }
  * { box-sizing: border-box; margin: 0; padding: 0; }
  html, body { width: 1200px; height: 753px; overflow: hidden; }
  body {
    background: var(--page-bg);
    font-family: "Ubuntu", sans-serif;
    color: var(--text-dark);
    position: relative;
  }
  .page { position: relative; width: 1200px; height: 753px; overflow: hidden; }

  /* account buttons */
  .account-links { position: absolute; top: 0; left: 940px; display: flex; gap: 4px; }
  .account-links a {
    display: block; width: 77px; height: 24px; line-height: 24px; text-align: center;
    background: linear-gradient(var(--brown-light), var(--brown));
    color: var(--white); font-size: 13px; font-weight: 500; text-decoration: none;
    border-radius: 0 0 5px 5px;
  }

  /* brand */
  .brand {
    position: absolute; left: 108px; top: 10px; width: 330px; height: 160px;
    display: flex; align-items: center; justify-content: center; gap: 10px;
  }
  .brand-mark { width: 14px; height: 14px; background: var(--brown); border-radius: 50%; }
  .brand-name { font-size: 34px; font-weight: 500; color: var(--brown); }

  /* contact */
  .contact { position: absolute; top: 52px; display: flex; gap: 7px; align-items: flex-start; }
  .contact.phone { left: 584px; }
  .contact.email { left: 869px; }
  .contact-icon {
    width: 37px; height: 37px; border-radius: 5px; background: var(--brown);
    display: flex; align-items: center; justify-content: center;
  }
  .contact-label { font-size: 14px; color: var(--tan); line-height: 16px; }
  .contact-value { font-size: 20px; font-style: italic; color: var(--tan); line-height: 22px; white-space: nowrap; }

  /* quote */
  .tagline {
    position: absolute; left: 558px; top: 110px; width: 540px; height: 70px;
    font-family: "Courgette", cursive; color: var(--brown); font-size: 17px;
    text-align: center; line-height: 23px; padding: 10px 14px 0 30px;
  }
  .tagline .mark { position: absolute; font-family: Georgia, serif; font-weight: 700; font-size: 52px; color: var(--tan); line-height: 1; }
  .tagline .mark.open { left: 0; top: -4px; }
  .tagline .mark.close { right: 0; top: 38px; }

  /* navigation */
  .main-nav {
    position: absolute; left: 114px; top: 193px; width: 984px; height: 43px;
    background: linear-gradient(var(--brown-light), var(--brown-dark));
    box-shadow: 0 4px 5px rgba(0,0,0,0.18);
    display: flex; align-items: center; padding-left: 24px;
  }
  .main-nav a {
    font-family: "Yesteryear", cursive; color: var(--white); text-decoration: none;
    font-size: 17px; white-space: nowrap;
  }
  .main-nav .sep { color: var(--white); margin: 0 12px; font-size: 16px; }

  /* content panel */
  .panel {
    position: absolute; left: 114px; top: 258px; width: 984px; height: 357px;
    background: linear-gradient(#f6f3ef, #ffffff 20%, #ffffff 80%, #f3efe9);
    border: 5px solid var(--white);
    box-shadow: 0 2px 8px rgba(0,0,0,0.2);
  }
  .panel-inner {
    position: absolute; left: 15px; top: 16px; width: 944px; height: 316px;
    border: 1px solid var(--tan-soft);
  }

  /* login */
  .login { position: absolute; left: 154px; top: 290px; width: 290px; }
  .login h2 { font-size: 15px; font-weight: 700; margin-bottom: 12px; }
  .login label { display: block; font-size: 13px; color: var(--text-dark); margin-bottom: 4px; }
  .field {
    height: 27px; border: 2px solid var(--field-border); background: var(--white);
    display: flex; align-items: center; justify-content: space-between; padding: 0 8px;
    margin-bottom: 18px; font-size: 13px; font-style: italic; color: #bbb;
  }
  .password-dots { display: flex; gap: 8px; }
  .password-dots span { width: 9px; height: 9px; border-radius: 50%; background: #ddd; }
  .login-options { display: flex; justify-content: space-between; align-items: center; font-size: 11px; margin-top: -2px; }
  .remember { display: flex; align-items: center; gap: 7px; }
  .checkbox { width: 13px; height: 13px; border: 1px solid #aaa; background: var(--white); }
  .forgot { color: var(--text-dark); text-decoration: underline; }
  .login-button {
    display: block; width: 100%; height: 32px; margin-top: 12px; border: 0; border-radius: 3px;
    background: linear-gradient(var(--brown-light), var(--brown));
    color: var(--white); font-family: "Ubuntu", sans-serif; font-size: 15px; font-weight: 500;
  }
  .login-social { margin-top: 8px; border-top: 2px solid var(--field-border); display: flex; justify-content: space-between; padding: 6px 14px 0 22px; font-size: 12px; }
  .social-group { text-align: center; }
  .ribbons { display: flex; gap: 6px; justify-content: center; margin-top: 6px; }
  .ribbon { width: 38px; height: 44px; }

  /* photo frames */
  .photo-back {
    position: absolute; left: 496px; top: 302px; width: 547px; height: 310px;
    background: #f6f1ec; border: 10px solid #f1ebe5; box-shadow: 0 1px 4px rgba(0,0,0,0.15);
  }
  .photo-back .fill { width: 100%; height: 100%; background: linear-gradient(#d8d3cc, #eeeae5); border: 2px solid #b0a89a; }
  .photo-tilted {
    position: absolute; left: 520px; top: 306px; width: 541px; height: 319px;
    transform: rotate(11.5deg); background: var(--white); padding: 11px;
    box-shadow: 0 3px 10px rgba(0,0,0,0.25);
  }
  .photo-tilted .photo-border { width: 100%; height: 100%; border: 2px solid var(--tan); padding: 3px; }
  .photo-tilted .photo-fill {
    width: 100%; height: 100%;
    background: radial-gradient(ellipse at 30% 20%, #d9a79c, transparent 45%), linear-gradient(135deg, #c9c2bb, #e9e6e2 50%, #8c8780);
  }

  /* footer */
  .site-footer { position: absolute; left: 0; top: 695px; width: 1200px; text-align: center; font-size: 11px; color: var(--text-mid); line-height: 14px; }
  .site-footer a { color: var(--text-mid); text-decoration: none; }
</style>
</head>
<body>
<div class="page">

  <nav class="account-links">
    <a href="#">Sign Up</a>
    <a href="#">Logout</a>
  </nav>

  <header>
    <div class="brand">
      <span class="brand-mark"></span>
      <span class="brand-name">Wedding Gleam</span>
    </div>

    <div class="contact phone">
      <div class="contact-icon">
        <svg width="22" height="20" viewBox="0 0 22 20"><path d="M2 6 Q11 0 20 6 L18 9 L15 7 L15 5 Q11 3.5 7 5 L7 7 L4 9 Z" fill="#fff"/><rect x="4" y="10" width="14" height="8" rx="1.5" fill="#fff"/><circle cx="11" cy="14" r="2" fill="#7e3f22"/></svg>
      </div>
      <div>
        <div class="contact-label">Call Us Now</div>
        <div class="contact-value">05823 - 917 - 346</div>
      </div>
    </div>

    <div class="contact email">
      <div class="contact-icon">
        <svg width="24" height="20" viewBox="0 0 24 20"><path d="M12 2 C5 2 2 6 2 9 C2 12 4 14 7 15 L6 19 L11 15.5 C18 16 22 12.5 22 9 C22 5 18 2 12 2 Z" fill="#fff"/></svg>
      </div>
      <div>
        <div class="contact-label">Email Us at</div>
        <div class="contact-value">hello@gleam.com</div>
      </div>
    </div>

    <blockquote class="tagline">
      <span class="mark open">“</span>
      There is no more lovely, friendly and charming relationship, communion or company than a good marriage.
      <span class="mark close">”</span>
    </blockquote>
  </header>

  <nav class="main-nav">
    <a href="#">Home</a><span class="sep">|</span>
    <a href="#">One Stop Registry</a><span class="sep">|</span>
    <a href="#">Wedding Deals</a><span class="sep">|</span>
    <a href="#">Travel/ Accommodation Getaway</a><span class="sep">|</span>
    <a href="#">Wedding marketplace</a><span class="sep">|</span>
    <a href="#">Gossip/Editorial</a><span class="sep">|</span>
    <a href="#">Booking Engine</a>
  </nav>

  <main class="panel">
    <div class="panel-inner"></div>
  </main>

  <div class="photo-back"><div class="fill"></div></div>
  <figure class="photo-tilted">
    <div class="photo-border">
      <div class="photo-fill" role="img" aria-label="Photo of bride and groom bottle stopper wedding favours on a table"></div>
    </div>
  </figure>

  <form class="login">
    <h2>Login</h2>
    <label>Username</label>
    <div class="field"><span>User Name....</span>
      <svg width="12" height="10" viewBox="0 0 12 10"><path d="M1 5 L4.5 8.5 L11 1" stroke="#ccc" stroke-width="2" fill="none"/></svg>
    </div>
    <label>Password</label>
    <div class="field">
      <span class="password-dots"><span></span><span></span><span></span><span></span><span></span><span></span><span></span><span></span></span>
      <svg width="12" height="10" viewBox="0 0 12 10"><path d="M1 5 L4.5 8.5 L11 1" stroke="#ccc" stroke-width="2" fill="none"/></svg>
    </div>
    <div class="login-options">
      <span class="remember"><span class="checkbox"></span>Remember Me</span>
      <a class="forgot" href="#">I forgot my password</a>
    </div>
    <button class="login-button" type="button">Let Me In Now!</button>
    <div class="login-social">
      <div class="social-group">
        Follow us at:
        <div class="ribbons">
          <svg class="ribbon" viewBox="0 0 38 44" role="img" aria-label="pallbook">
            <path d="M0 0 H38 V44 L19 36 L0 44 Z" fill="#d8c3ad"/>
            <text x="19" y="22" text-anchor="middle" font-family="Ubuntu, sans-serif" font-size="7" fill="#fff">pallbook</text>
          </svg>
          <svg class="ribbon" viewBox="0 0 38 44" role="img" aria-label="chirpline">
            <path d="M0 0 H38 V44 L19 36 L0 44 Z" fill="#d8c3ad"/>
            <text x="19" y="22" text-anchor="middle" font-family="Ubuntu, sans-serif" font-size="7" fill="#fff">chirpline</text>
          </svg>
        </div>
      </div>
      <div class="social-group">
        Subscribe to mail:
        <div class="ribbons">
          <svg class="ribbon" viewBox="0 0 38 44" role="img" aria-label="Mailing list">
            <path d="M0 0 H38 V44 L19 36 L0 44 Z" fill="#d8c3ad"/>
            <rect x="9" y="12" width="20" height="14" fill="none" stroke="#fff" stroke-width="2"/>
            <path d="M9 12 L19 20 L29 12" fill="none" stroke="#fff" stroke-width="2"/>
          </svg>
        </div>
      </div>
    </div>
  </form>

  <footer class="site-footer">
    <a href="#">About Wedding Gleam</a> | <a href="#">Advertise with Us</a> | <a href="#">Contact Us</a> | <a href="#">Terms &amp; Conditions</a> | <a href="#">Privacy Policy</a><br>
    Copyright © 2012 Wedding Gleam
  </footer>

</div>
</body>
</html>
```